2-page digital brochure highlighting company and service offerings to oil and gas market in W Canada

we are asked to send a quick info package to potential clients. Brief description of who Harrowfield Conduit Corp is and what we can offer our Oil & Gas, Midstream and engineering prospects. Our services include ; pipeline maintenance and integrity, abandonments and decommissioning, and project management. PP attached for pictures and verbiage. Branding guidelines below. want to promote services and safety

```html
<!DOCTYPE html>
<html lang="en">
<head>
<meta charset="utf-8">
<title>Harrowfield Conduit Corp – Brochure</title>
<link href="https://fonts.googleapis.com/css2?family=Poppins:wght@400;500;600;700;800;900&display=swap" rel="stylesheet">
<style>
:root{
  --navy:#0d4766;
  --navy-deep:#0a3a55;
  --orange:#e8891c;
  --ink:#1f3b4d;
  --paper:#ffffff;
  --backdrop:#dcdcdc;
}
*{margin:0;padding:0;box-sizing:border-box}
html,body{width:1200px;height:2970px;overflow:hidden;background:var(--backdrop);font-family:'Poppins',sans-serif;color:var(--ink)}
.page{position:absolute;left:139.5px;width:921px;height:1303px;background:var(--paper);overflow:hidden;box-shadow:0 4px 18px rgba(0,0,0,.18)}
.page-one{top:139.5px}
.page-two{top:1528.5px}
.abs{position:absolute}
.layer{position:absolute;left:0;top:0}

/* brand */
.brand{left:54px;top:44px;display:flex;align-items:center;gap:16px}
.brand-mark{width:46px;height:46px;background:var(--navy)}
.brand-name{font-weight:700;font-size:40px;color:var(--navy);letter-spacing:1px}
.brand-small{right:8px;top:122px;display:flex;align-items:center;gap:6px}
.brand-small .brand-mark{width:14px;height:14px}
.brand-small .brand-name{font-size:14px;letter-spacing:0}

.headline{left:48px;top:138px;font-weight:800;font-size:62px;line-height:55px;color:#fff;letter-spacing:-.5px}

/* section titles */
.section-title{font-weight:800;font-size:32px;color:var(--navy);letter-spacing:-.3px;white-space:nowrap}
.section-title em{font-style:normal;color:var(--orange)}

/* tick lists */
.ticks{list-style:none}
.ticks li{position:relative;padding-left:25px;font-size:12px;line-height:15px}
.ticks li::before{content:"";position:absolute;left:0;top:2px;width:11px;height:11px;border-radius:50%;background:var(--orange)}
.ticks li::after{content:"";position:absolute;left:3.5px;top:4px;width:3px;height:5px;border:solid #fff;border-width:0 1.5px 1.5px 0;transform:rotate(45deg)}
.story{left:51px;top:376px;width:820px}
.story li{margin-bottom:14px}

/* features */
.feature-head{display:flex;align-items:center;gap:14px}
.feature-icon{width:52px;height:52px;flex:none}
.feature-title{font-weight:700;font-size:22px;color:var(--navy);white-space:nowrap}
.feature-text{font-size:11.5px;line-height:14.5px;margin-top:10px;width:412px}

/* services */
.service-label{font-size:14px;line-height:16px;color:var(--navy);font-weight:500}
.service-label.left{text-align:right}
.hub-text{left:341px;top:990px;width:200px;text-align:center;font-weight:700;font-size:25px;line-height:29px;color:var(--navy)}

/* footer */
.footer{left:0;top:1217px;width:921px;height:86px}
.footer-phone{left:34px;top:1230px;font-weight:700;font-size:25px;color:#fff;display:flex;align-items:center;gap:9px}
.footer-web{left:34px;top:1266px;font-size:14px;color:#fff;display:flex;align-items:center;gap:9px;white-space:nowrap}
.footer-ops{left:317px;top:1228px;font-size:13px;line-height:15.5px;color:#fff}
.footer-ops .lbl{color:var(--orange)}
.footer-addr{top:1244px;font-size:13.5px;line-height:16.5px;color:#fff;font-weight:500;display:flex;gap:9px}
.footer-addr svg{margin-top:2px;flex:none}

/* page two */
.safety-list{left:51px;top:100px;width:450px}
.safety-list li{color:#fff;font-size:12px;line-height:15px;position:absolute;width:450px;left:0}
.photo{border-radius:10px}
.body-list li{font-size:16px;line-height:18.5px;padding-left:25px}
.body-list li::before{top:4px}
.body-list li::after{top:6px}
</style>
</head>
<body>

<!-- ===================== PAGE ONE ===================== -->
<section class="page page-one">
  <svg class="layer" width="921" height="317" viewBox="0 0 921 317">
    <defs>
      <linearGradient id="sunsetSky" x1="0" y1="0" x2="0" y2="1">
        <stop offset="0" stop-color="#6f8fb8"/>
        <stop offset=".55" stop-color="#b7a58f"/>
        <stop offset=".85" stop-color="#e69a4a"/>
        <stop offset="1" stop-color="#3a3630"/>
      </linearGradient>
    </defs>
    <polygon points="0,128 478,128 473,137 560,317 0,317" fill="var(--navy)"/>
    <polygon points="577,0 921,0 921,317 572,317 484,137" fill="var(--orange)"/>
    <polygon points="583,0 921,0 921,317 578,317 491,137" fill="url(#sunsetSky)" role="img" aria-label="Photo of an excavator on a wellsite at sunset"/>
  </svg>

  <div class="abs brand"><span class="brand-mark"></span><span class="brand-name">Harrowfield</span></div>
  <div class="abs brand-small"><span class="brand-mark"></span><span class="brand-name">Harrowfield</span></div>

  <h1 class="abs headline">Focused.<br>Collaborative.<br>Safe.</h1>

  <h2 class="abs section-title" style="left:51px;top:328px">THE HARROWFIELD <em>STORY</em></h2>
  <ul class="abs ticks story">
    <li>Harrowfield (HCC) is borne out of a belief in executing differently.</li>
    <li style="margin-bottom:16px">Innovation lives at the intersection of experience and expertise and HCC is focused there.</li>
    <li>HCC is built on long-standing relationships within Industry and across domains and disciplines. These connections are what makes Harrowfield Conduit unique.</li>
  </ul>

  <h2 class="abs section-title" style="left:51px;top:477px">WHY <em>HARROWFIELD</em></h2>

  <!-- features -->
  <div class="abs" style="left:48px;top:520px">
    <div class="feature-head">
      <svg class="feature-icon" viewBox="0 0 52 52"><circle cx="26" cy="26" r="24" fill="var(--orange)" stroke="var(--navy)" stroke-width="3"/><circle cx="19" cy="20" r="5" fill="var(--navy)"/><circle cx="33" cy="20" r="5" fill="var(--navy)"/><path d="M10 37a9 8 0 0 1 18 0zM24 37a9 8 0 0 1 18 0z" fill="var(--navy)"/></svg>
      <span class="feature-title">100% ENGAGEMENT</span>
    </div>
    <p class="feature-text">Our field personnel ensure accurate costing and scheduling through involvement from inception to completion of your project.</p>
  </div>
  <div class="abs" style="left:483px;top:520px">
    <div class="feature-head">
      <svg class="feature-icon" viewBox="0 0 52 52"><circle cx="26" cy="26" r="24" fill="var(--orange)" stroke="var(--navy)" stroke-width="3"/><rect x="16" y="13" width="18" height="25" rx="2" fill="none" stroke="var(--navy)" stroke-width="2.5"/><path d="M20 20h10M20 25h10M20 30h6" stroke="var(--navy)" stroke-width="2"/><circle cx="34" cy="35" r="5" fill="none" stroke="var(--navy)" stroke-width="2.5"/></svg>
      <span class="feature-title">TRANSPARENCY</span>
    </div>
    <p class="feature-text">The Harrowfield culture is based on transparency and visibility to the client.</p>
  </div>
  <div class="abs" style="left:48px;top:622px">
    <div class="feature-head">
      <svg class="feature-icon" viewBox="0 0 52 52"><circle cx="26" cy="26" r="24" fill="var(--orange)" stroke="var(--navy)" stroke-width="3"/><rect x="14" y="14" width="24" height="14" rx="2" fill="none" stroke="var(--navy)" stroke-width="2.5"/><circle cx="18" cy="34" r="3.5" fill="var(--navy)"/><circle cx="34" cy="34" r="3.5" fill="var(--navy)"/><path d="M12 42a6 5 0 0 1 12 0zM28 42a6 5 0 0 1 12 0z" fill="var(--navy)"/></svg>
      <span class="feature-title">EXPERT ADVICE</span>
    </div>
    <p class="feature-text">Our technical experts and field personnel’s competency provides the right solution for your needs. Experience proactively drives the business process.</p>
  </div>
  <div class="abs" style="left:483px;top:622px">
    <div class="feature-head">
      <svg class="feature-icon" viewBox="0 0 52 52"><circle cx="26" cy="26" r="24" fill="var(--orange)" stroke="var(--navy)" stroke-width="3"/><circle cx="26" cy="26" r="14" fill="var(--navy)"/><path d="M26 17v10l6 4" stroke="var(--orange)" stroke-width="3" fill="none" stroke-linecap="round"/></svg>
      <span class="feature-title">ON TIME</span>
    </div>
    <p class="feature-text">Harrowfield provides on time and on budget project delivery through accountability for time and resources.</p>
  </div>
  <div class="abs" style="left:48px;top:738px">
    <div class="feature-head">
      <svg class="feature-icon" viewBox="0 0 52 52"><circle cx="26" cy="26" r="24" fill="var(--orange)" stroke="var(--navy)" stroke-width="3"/><circle cx="23" cy="26" r="12" fill="var(--navy)"/><text x="23" y="32" text-anchor="middle" font-family="Poppins,sans-serif" font-weight="700" font-size="17" fill="var(--orange)">$</text><path d="M37 16v20" stroke="var(--navy)" stroke-width="3"/></svg>
      <span class="feature-title">ACCURATE COST REPORTING</span>
    </div>
    <p class="feature-text">Implementing project specific quality control programs and a rigorous management of change process drives project cost certainty.</p>
  </div>
  <div class="abs" style="left:483px;top:738px">
    <div class="feature-head">
      <svg class="feature-icon" viewBox="0 0 52 52"><circle cx="26" cy="26" r="24" fill="var(--orange)" stroke="var(--navy)" stroke-width="3"/><circle cx="26" cy="17" r="6" fill="var(--navy)"/><path d="M23 17l2 2 4-4" stroke="var(--orange)" stroke-width="2" fill="none"/><path d="M11 32l8-6 7 4 7-4 8 6-7 7h-16z" fill="var(--navy)"/></svg>
      <span class="feature-title">TRUSTED RELATIONSHIPS</span>
    </div>
    <p class="feature-text">Gain the certainty of established and supportive subcontractor relationships. Harrowfield exceeds expectations through project collaboration as a stakeholder rather than a vendor</p>
  </div>

  <!-- service offerings -->
  <svg class="layer" width="921" height="1303" viewBox="0 0 921 1303">
    <g>
      <circle cx="441.5" cy="1020" r="92" fill="none" stroke="var(--navy)" stroke-width="13"/>
      <circle cx="441.5" cy="1020" r="79" fill="#fff" stroke="var(--orange)" stroke-width="7"/>
    </g>
    <g fill="var(--navy)" stroke="var(--orange)" stroke-width="4">
      <circle cx="334" cy="896" r="26"/><circle cx="278" cy="950" r="26"/><circle cx="274" cy="1020" r="26"/><circle cx="277" cy="1093" r="26"/><circle cx="333" cy="1150" r="26"/>
      <circle cx="550" cy="896" r="26"/><circle cx="607.5" cy="950" r="26"/><circle cx="611" cy="1020" r="26"/><circle cx="608.5" cy="1093" r="26"/><circle cx="553" cy="1150" r="26"/>
    </g>
    <g fill="none" stroke="#fff" stroke-width="2.5" stroke-linecap="round">
      <circle cx="334" cy="896" r="10" stroke-dasharray="4 3" stroke-width="5"/><circle cx="334" cy="896" r="4"/>
      <rect x="266" y="944" width="24" height="12" rx="1"/><path d="M266 960h24"/>
      <rect x="266" y="1008" width="16" height="22" rx="1"/><path d="M270 1015h8M270 1020h8"/><circle cx="284" cy="1028" r="4"/>
      <path d="M265 1102v-8h24v8M270 1094a7 7 0 0 1 14 0"/><circle cx="277" cy="1084" r="4"/>
      <rect x="324" y="1138" width="18" height="24" rx="3"/>
      <circle cx="550" cy="896" r="11"/><path d="M550 883v26M537 896h26"/>
      <rect x="597" y="940" width="21" height="20" rx="2"/><path d="M601 947h13M601 953h13"/>
      <path d="M601 1013l20 20M621 1013l-20 20"/>
      <circle cx="603" cy="1097" r="6" stroke-dasharray="3 2" stroke-width="4"/><circle cx="615" cy="1087" r="4" stroke-dasharray="2 2" stroke-width="3"/>
      <path d="M544 1158l8-16 10 6-6 12z"/>
    </g>
    <text x="333" y="1153.5" text-anchor="middle" font-family="Poppins,sans-serif" font-size="7" font-weight="700" fill="#fff">HDD</text>
  </svg>
  <div class="abs hub-text">SERVICE<br>OFFERINGS</div>

  <div class="abs service-label left" style="right:653px;top:868px">Repair and<br>Rehabilitation</div>
  <div class="abs service-label left" style="right:696px;top:925px">Decommissioning<br>and Abandonment</div>
  <div class="abs service-label left" style="right:696px;top:998px">Coating<br>application</div>
  <div class="abs service-label left" style="right:696px;top:1075px">Geohazard<br>management</div>
  <div class="abs service-label left" style="right:653px;top:1140px">HDD<br>Support</div>
  <div class="abs service-label" style="left:613px;top:869px">Integrity<br>Verification Dig</div>
  <div class="abs service-label" style="left:665px;top:925px">Program Management<br>and Execution</div>
  <div class="abs service-label" style="left:665px;top:998px">Watercourse<br>crossing repair</div>
  <div class="abs service-label" style="left:665px;top:1076px">Engineering and<br>project management</div>
  <div class="abs service-label" style="left:613px;top:1141px">In-line inspection<br>program support</div>

  <!-- footer -->
  <svg class="abs footer" viewBox="0 0 921 86">
    <rect width="921" height="86" fill="var(--navy)"/>
    <polygon points="0,0 266,0 254,86 0,86" fill="var(--orange)"/>
    <polygon points="266,0 274,0 262,86 254,86" fill="#fff"/>
  </svg>
  <div class="abs footer-phone"><svg width="16" height="16" viewBox="0 0 16 16"><path d="M3 1l3 3-2 2c1 2 3 4 5 5l2-2 3 3-2 3C6 14 2 10 1 3z" fill="#fff"/></svg>(587) 555-0142</div>
  <div class="abs footer-web"><svg width="14" height="14" viewBox="0 0 14 14"><circle cx="7" cy="7" r="6" fill="none" stroke="#fff" stroke-width="1.5"/><path d="M1 7h12M7 1c-3 3-3 9 0 12M7 1c3 3 3 9 0 12" fill="none" stroke="#fff"/></svg>www.harrowfieldcorp.com</div>
  <div class="abs footer-ops"><span class="lbl">Operations:</span><br>&#9990; 403-555-0187.<br><span class="lbl">Business Development:</span><br>&#9990; 403-555-0163.</div>
  <div class="abs footer-addr" style="left:507px"><svg width="12" height="15" viewBox="0 0 12 15"><path d="M6 14S1 8.5 1 5.5a5 5 0 0 1 10 0C11 8.5 6 14 6 14z" fill="none" stroke="#fff" stroke-width="1.6"/><circle cx="6" cy="5.5" r="1.8" fill="#fff"/></svg><span>418 Ridgeline Ave East,<br>Sundre, Alberta</span></div>
  <div class="abs footer-addr" style="left:686px"><svg width="12" height="15" viewBox="0 0 12 15"><path d="M6 14S1 8.5 1 5.5a5 5 0 0 1 10 0C11 8.5 6 14 6 14z" fill="none" stroke="#fff" stroke-width="1.6"/><circle cx="6" cy="5.5" r="1.8" fill="#fff"/></svg><span>250 9 Ave SW, Suite 1400<br>Calgary, Alberta T2P0X1</span></div>
</section>

<!-- ===================== PAGE TWO ===================== -->
<section class="page page-two">
  <svg class="layer" width="921" height="384" viewBox="0 0 921 384">
    <defs>
      <linearGradient id="digSite" x1="0" y1="0" x2="0" y2="1">
        <stop offset="0" stop-color="#6d9ad0"/>
        <stop offset=".35" stop-color="#a9bfd6"/>
        <stop offset=".5" stop-color="#9a7a55"/>
        <stop offset="1" stop-color="#6b5038"/>
      </linearGradient>
    </defs>
    <rect width="921" height="380" fill="var(--navy)"/>
    <polygon points="592,0 921,0 921,380 592,380 477,189" fill="#fff"/>
    <polygon points="599,0 921,0 921,380 599,380 484,189" fill="url(#digSite)" role="img" aria-label="Photo of an excavator digging a deep trench"/>
    <rect y="380" width="921" height="4" fill="var(--orange)"/>
  </svg>

  <h2 class="abs section-title" style="left:51px;top:38px;color:#fff">SAFETY</h2>
  <ul class="abs ticks safety-list">
    <li style="top:0">Prairie Construction Safety Council-certified industry leading safety program.</li>
    <li style="top:45px">Orienting new employees and implementing Competency Training is essential for safety.</li>
    <li style="top:90px">The team is composed of seasoned professionals and dedicated individuals.</li>
    <li style="top:133px">For maintaining COR certification, we conduct monthly meetings, annual internal audits, and an external audit every three years.</li>
    <li style="top:185px">Registered with SiteLedger, VendorCheck &amp; Qualivo.</li>
    <li style="top:220px">We offer Workers Compensation accounts in the provinces of British Columbia, Alberta, Saskatchewan, and Manitoba.</li>
  </ul>

  <!-- pipeline integrity -->
  <div class="abs photo" style="left:51px;top:419px;width:184px;height:158px;background:linear-gradient(180deg,#4f86c9 0%,#a7c4e2 45%,#d8d6cf 70%,#8b7a62 100%)" role="img" aria-label="Photo of an excavator working on a snowy pipeline site"></div>
  <h2 class="abs section-title" style="left:254px;top:404px">PIPELINE <em>INTEGRITY</em></h2>
  <ul class="abs ticks body-list" style="left:254px;top:458px;width:630px">
    <li style="margin-bottom:19px">Services include operation, inspection, maintenance, HSE and corporate communications</li>
    <li style="margin-bottom:19px">Integrity excavation services including locating, excavating, hand exposing, coating removal and sandblasting</li>
    <li style="margin-bottom:19px">Coating application</li>
    <li>Repair and replacement services, cut-out sleeve installation, sleeve repairs and pipeline lowering</li>
  </ul>

  <!-- abandonment -->
  <h2 class="abs section-title" style="left:51px;top:677px">PIPELINE ABANDONMENT <em>&amp; DECOMMISSIONING</em></h2>
  <ul class="abs ticks body-list" style="left:51px;top:745px;width:620px">
    <li style="margin-bottom:18.5px">Pipeline pigging and purging services</li>
    <li style="margin-bottom:18.5px">Pipeline branch termination and dead leg elimination</li>
    <li style="margin-bottom:18.5px">Pipeline abandonments</li>
    <li>Purging and disposal of surface and subsurface production equipment</li>
  </ul>
  <div class="abs photo" style="left:681px;top:744px;width:190px;height:145px;background:linear-gradient(180deg,#5d87c0 0%,#b9cce0 45%,#e6e9ee 70%,#9fa5ab 100%)" role="img" aria-label="Photo of a service truck beside pipeline equipment in snow"></div>

  <!-- in-line inspection -->
  <h2 class="abs section-title" style="left:51px;top:927px">IN-LINE INSPECTION <em>SUPPORT</em></h2>
  <div class="abs photo" style="left:51px;top:1002px;width:190px;height:174px;background:linear-gradient(180deg,#3f7cc6 0%,#9fc0e3 45%,#e9e9e6 62%,#a89a7c 100%)" role="img" aria-label="Photo of a field worker beside a service truck and pipe risers"></div>
  <ul class="abs ticks body-list" style="left:275px;top:999px;width:600px">
    <li style="margin-bottom:10.5px">Pre-job scouting and estimates</li>
    <li style="margin-bottom:10.5px">Access planning, logistics and construction</li>
    <li style="margin-bottom:9px">Full scale coordination and collaborative abandonment program management across internal and external stakeholders</li>
    <li style="margin-bottom:10.5px">Construction supervision and monitoring</li>
    <li style="margin-bottom:10.5px">Surface and subsurface information gathering</li>
    <li>Land packages</li>
  </ul>

  <!-- footer -->
  <svg class="abs footer" viewBox="0 0 921 86">
    <rect width="921" height="86" fill="var(--navy)"/>
    <polygon points="0,0 266,0 254,86 0,86" fill="var(--orange)"/>
    <polygon points="266,0 274,0 262,86 254,86" fill="#fff"/>
  </svg>
  <div class="abs footer-phone"><svg width="16" height="16" viewBox="0 0 16 16"><path d="M3 1l3 3-2 2c1 2 3 4 5 5l2-2 3 3-2 3C6 14 2 10 1 3z" fill="#fff"/></svg>(587) 555-0142</div>
  <div class="abs footer-web"><svg width="14" height="14" viewBox="0 0 14 14"><circle cx="7" cy="7" r="6" fill="none" stroke="#fff" stroke-width="1.5"/><path d="M1 7h12M7 1c-3 3-3 9 0 12M7 1c3 3 3 9 0 12" fill="none" stroke="#fff"/></svg>www.harrowfieldcorp.com</div>
  <div class="abs footer-ops"><span class="lbl">Operations:</span><br>&#9990; 403-555-0187.<br><span class="lbl">Business Development:</span><br>&#9990; 403-555-0163.</div>
  <div class="abs footer-addr" style="left:507px"><svg width="12" height="15" viewBox="0 0 12 15"><path d="M6 14S1 8.5 1 5.5a5 5 0 0 1 10 0C11 8.5 6 14 6 14z" fill="none" stroke="#fff" stroke-width="1.6"/><circle cx="6" cy="5.5" r="1.8" fill="#fff"/></svg><span>418 Ridgeline Ave East,<br>Sundre, Alberta</span></div>
  <div class="abs footer-addr" style="left:686px"><svg width="12" height="15" viewBox="0 0 12 15"><path d="M6 14S1 8.5 1 5.5a5 5 0 0 1 10 0C11 8.5 6 14 6 14z" fill="none" stroke="#fff" stroke-width="1.6"/><circle cx="6" cy="5.5" r="1.8" fill="#fff"/></svg><span>250 9 Ave SW, Suite 1400<br>Calgary, Alberta T2P0X1</span></div>
</section>

</body>
</html>
```